Modern & Fresh Sumeray Book Cover

Need a creative e-book cover for my book.

Title: Get Sumeray Sorted
Subtitle: Learn How To Easily Choose & Enroll in the Perfect Coverage at the Perfect Time.

Target Market(s)

60-70 year olds in the United States

Font styles to use
Sans Serif

Colors
9bcb3c
33a6d7

Requirements
Must have
• Must look modern and fresh.
• Use our company colors www.BrovaMint.com

```html
<!DOCTYPE html>
<html lang="en">
<head>
<meta charset="utf-8">
<title>Get Sumeray Sorted — Book Cover</title>
<link rel="stylesheet" href="https://fonts.googleapis.com/css2?family=Bebas+Neue&family=Cormorant+SC:wght@500;600&display=swap">
<style>
  :root {
    --navy-deep: #0b1838;
    --navy-mid: #1c3570;
    --title-green: #a3cf3a;
    --accent-blue: #33a6d7;
    --text-white: #ffffff;
  }
  html, body {
    margin: 0;
    padding: 0;
    width: 802px;
    height: 1200px;
    overflow: hidden;
    background: var(--navy-deep);
  }
  .cover {
    position: relative;
    width: 802px;
    height: 1200px;
    overflow: hidden;
    background: radial-gradient(ellipse 75% 60% at 50% 50%, var(--navy-mid) 0%, #142a5c 45%, var(--navy-deep) 100%);
  }
  .cover__title {
    position: absolute;
    top: 48px;
    left: 0;
    width: 100%;
    margin: 0;
    text-align: center;
    font-family: "Bebas Neue", "Oswald", sans-serif;
    font-weight: 400;
    font-size: 134px;
    line-height: 108px;
    letter-spacing: 2px;
    color: var(--title-green);
    text-transform: uppercase;
  }
  .cover__subtitle {
    position: absolute;
    top: 292px;
    left: 0;
    width: 100%;
    margin: 0;
    text-align: center;
    font-family: "Cormorant SC", "Cormorant Garamond", serif;
    font-weight: 600;
    font-size: 33px;
    line-height: 40px;
    color: var(--text-white);
  }
  .cover__rule {
    position: absolute;
    left: 0;
    width: 100%;
    height: 9px;
    background: var(--accent-blue);
  }
  .cover__rule--top { top: 498px; }
  .cover__rule--bottom { top: 798px; }
  .cover__emblem {
    position: absolute;
    top: 548px;
    left: 241px;
    width: 320px;
    height: 212px;
  }
  .cover__author {
    position: absolute;
    top: 1092px;
    left: 0;
    width: 100%;
    margin: 0;
    text-align: center;
    font-family: "Bebas Neue", "Oswald", sans-serif;
    font-size: 62px;
    letter-spacing: 5px;
    color: var(--text-white);
    text-transform: uppercase;
  }
</style>
</head>
<body>
  <main class="cover">
    <h1 class="cover__title">Get Sumeray<br>Sorted</h1>
    <p class="cover__subtitle">Learn How To Easily Choose &amp; Enroll<br>in the Perfect Coverage at the Perfect Time</p>

    <div class="cover__rule cover__rule--top"></div>

    <svg class="cover__emblem" viewBox="0 0 320 212" role="img" aria-label="Light blue winged medical staff emblem">
      <defs>
        <radialGradient id="emblemGlow" cx="50%" cy="45%" r="60%">
          <stop offset="0%" stop-color="#33a6d7" stop-opacity="0.55"/>
          <stop offset="100%" stop-color="#33a6d7" stop-opacity="0"/>
        </radialGradient>
      </defs>
      <rect x="0" y="0" width="320" height="212" rx="30" fill="url(#emblemGlow)"/>
    </svg>

    <div class="cover__rule cover__rule--bottom"></div>

    <p class="cover__author">Author's Name</p>
  </main>
</body>
</html>
```